agricultural technology company needs business cards*

design a business card that represents our business well. please see our website: vastrelbyfieldseal.com.au
professional, simple, clean lines, not complicated or floral.....

```html
<!DOCTYPE html>
<html lang="en">
<head>
<meta charset="utf-8">
<title>Vastrelby FieldSeal – Business Card</title>
<link href="https://fonts.googleapis.com/css2?family=Lato:wght@400;700;900&display=swap" rel="stylesheet">
<style>
  :root {
    --backdrop: #dcdde1;
    --green-deep: #86b22c;
    --green-light: #acd34a;
    --brand-green: #2aa84a;
    --brand-navy: #1d2a5c;
    --ink: #2b2b2b;
    --white: #ffffff;
    --card-shadow: 0 12px 18px rgba(0, 0, 0, 0.22);
  }
  * { margin: 0; padding: 0; box-sizing: border-box; }
  html, body {
    width: 1200px;
    height: 800px;
    overflow: hidden;
    background: var(--backdrop);
    font-family: "Lato", sans-serif;
  }
  .canvas {
    position: relative;
    width: 1200px;
    height: 800px;
  }
  .card {
    position: absolute;
    left: 389px;
    width: 461px;
    height: 263px;
    box-shadow: var(--card-shadow);
  }
  .card--front {
    top: 93px;
    background: linear-gradient(225deg, var(--green-light) 0%, var(--green-deep) 100%);
  }
  .card--back {
    top: 422px;
    background: var(--white);
  }

  /* Front */
  .front-wordmark {
    position: absolute;
    left: 0;
    right: 0;
    top: 96px;
    text-align: center;
    color: var(--white);
    font-weight: 900;
    font-size: 34px;
    line-height: 1;
    letter-spacing: -0.5px;
  }
  .front-url {
    position: absolute;
    left: 0;
    right: 0;
    top: 222px;
    text-align: center;
    color: var(--white);
    font-size: 12px;
    letter-spacing: 0.2px;
  }

  /* Back */
  .back-brand {
    position: absolute;
    left: 50px;
    top: 114px;
    display: flex;
    align-items: center;
    gap: 10px;
  }
  .back-brand__name {
    color: var(--brand-navy);
    font-weight: 900;
    font-size: 21px;
    line-height: 1;
    letter-spacing: -0.4px;
  }
  .back-brand__mark {
    width: 26px;
    height: 26px;
    flex: none;
    background: var(--brand-green);
  }
  .back-divider {
    position: absolute;
    left: 235px;
    top: 72px;
    width: 1px;
    height: 120px;
    background: var(--brand-green);
  }
  .contact {
    position: absolute;
    left: 249px;
    top: 70px;
    color: var(--ink);
    font-size: 11.5px;
    line-height: 1.4;
  }
  .contact__name {
    color: var(--brand-green);
    font-weight: 700;
    font-size: 16px;
    line-height: 1.2;
  }
  .contact__role { margin-bottom: 8px; }
  .contact__address { margin-bottom: 8px; line-height: 1.4; }
  .contact__line {
    display: flex;
    align-items: center;
    gap: 5px;
    line-height: 1.25;
  }
  .contact__icon {
    width: 9px;
    height: 9px;
    flex: none;
  }
</style>
</head>
<body>
<main class="canvas">

  <section class="card card--front" aria-label="Business card front">
    <div class="front-wordmark">Vastrelby<br>FieldSeal</div>
    <p class="front-url">www.vastrelbyfieldseal.com.au</p>
  </section>

  <section class="card card--back" aria-label="Business card back">
    <div class="back-brand">
      <span class="back-brand__name">Vastrelby<br>FieldSeal</span>
      <span class="back-brand__mark"></span>
    </div>

    <div class="back-divider"></div>

    <div class="contact">
      <p class="contact__name">Maren Ostholt</p>
      <p class="contact__role">Director</p>
      <p class="contact__address">52 Harwick Road<br>Kellerton, WA 6170</p>
      <p class="contact__line">
        <svg class="contact__icon" viewBox="0 0 10 10" aria-hidden="true">
          <path d="M2.2 0.6 L3.6 2.6 L2.7 3.6 Q3.6 5.6 6.3 7.2 L7.3 6.3 L9.4 7.7 L8.4 9.4 Q4.8 9.4 2.3 6.9 Q0.4 4.6 0.6 1.6 Z" fill="#2aa84a"/>
        </svg>
        1300 482 619
      </p>
      <p class="contact__line">
        <svg class="contact__icon" viewBox="0 0 10 10" aria-hidden="true">
          <rect x="0.5" y="2" width="9" height="6.5" fill="#2aa84a"/>
          <path d="M0.8 2.3 L5 5.6 L9.2 2.3" stroke="#ffffff" stroke-width="0.9" fill="none"/>
        </svg>
        vastrelbyfieldseal@com.au
      </p>
      <p class="contact__line">
        <svg class="contact__icon" viewBox="0 0 10 10" aria-hidden="true">
          <circle cx="5" cy="5" r="4.3" fill="none" stroke="#2aa84a" stroke-width="0.9"/>
          <ellipse cx="5" cy="5" rx="1.8" ry="4.3" fill="none" stroke="#2aa84a" stroke-width="0.8"/>
          <path d="M0.8 5 H9.2 M1.6 3 H8.4 M1.6 7 H8.4" stroke="#2aa84a" stroke-width="0.7"/>
        </svg>
        vastrelbyfieldseal.com.au
      </p>
    </div>
  </section>

</main>
</body>
</html>
```